Local Chiropractoc needs Modern Website

This website needs to have an upscale look with a very modern feel.

This is for a home page psd layout and an interior page psd file so 2 files total

Below is the information and websites to reference

Add Logo that is attached.

Build a color scheme similar to this website image titled "chiro-1" using the golds, whites, blacks and browns from the color of the logo

I want to see a light background so it makes the images and logo stick out

Must Include these pages in a horizontal menu bar in this order:
Home, Why Brightmoor?, How Chiropractic Helps, Ask the Doctor, Work Place Wellness, Request an Appointment, Blog, Contact Us

Please add the following social media logos to the top and footer of the website: Chatterly, Vexora+, Streamlo

Build a "classy looking" Make An Appointment Button into the header with the contact info below

Phone Number:
555-014-2739

Address:
4128 North Tamsin Blvd, Suite #7
Harrowfield, GA 30917

This website needs 4 rotating banners. Please reference a layout similar to this for the banners: http://quarrelstonechiro.example/. However design it nicer than this website

Below are the description for each banner

Rotating Banner #1
Use Image: Patients are Saying
Add a line of text: "What our Patients are Saying"

Rotating Banner #2
Use Image: Becoming a Patient
Add a line of text: "Interested in Becoming a Patient"

Rotating Banner #3
Use Image: Dinner with Doctor
Add a line of text: "Win A free Dinner with Dr. Halloway"

Rotating Banner #4
Use Image: Chatterly
Add a line of text: Follow us on Chatterly
Bullet point these 4 lines underneath the "Follow us on Chatterly" text:
- Cutting Edge Health News
- Healthy Recipes
- Newest Health Products
- Clinic Events

I'd like to see a free consultation box similar to the "chiro-1" image. Fields to include are: First Name, Last Name, Phone Number, Comments

For the body, please fill it with latin text. Please design a professional 2 column layout similar to the www.quarrelstonechiro.example website. (DO NOT COPY THIS WEBSITE, USE IT AS REFERENCE)

In the left column include in this order:
Video
Rate us on Vexora Button, Find us on Chatterly Button
Welcome Letter

In the right column include this:

Office Hours
Monday: 8:00-11:00, 2:00-5:00
Tuesday: 8:30-11:00, 2:00-5:30
Wednesday: 8:00-11:00, 2:00-5:00
Thursday: 10:00-12:00, 2:30-5:00
Friday: 8:00-10:00, 1:00-5:00
Saturday: Closed
Sunday: Closed

Patient Testimonials
Fill with a latin text testimonial. This spot will rotate different testimonials

For the footer please design something similar to the layout of this: http://www.verdantpathspinecare.example/

Also include in the Footer: Powered by Pixelmere Web Group

```html
<!DOCTYPE html>
<html lang="en">
<head>
<meta charset="utf-8">
<title>Brightmoor Chiropractic</title>
<link rel="stylesheet" href="https://fonts.googleapis.com/css2?family=Open+Sans:ital,wght@0,400;0,600;0,700;0,800;1,400&display=swap">
<style>
:root{
  --gold:#a8894e;
  --gold-light:#cbb078;
  --gold-dark:#7a6131;
  --ink:#161616;
  --charcoal:#2b2b2b;
  --text:#4a4a4a;
  --muted:#9a9a9a;
  --rule:#d9cdb4;
  --paper:#ffffff;
  --footer-grey:#e4e4e4;
  --footer-gold:#a88c52;
}
*{margin:0;padding:0;box-sizing:border-box}
html,body{width:755px;height:1200px;overflow:hidden;background:var(--paper)}
body{position:relative;font-family:"Open Sans",Arial,sans-serif;color:var(--text)}
.abs{position:absolute}

/* header */
.brand{position:absolute;display:flex;align-items:center;gap:5px}
.brand-square{width:8px;height:22px;background:var(--ink)}
.brand-name{font-weight:800;font-size:13px;color:var(--ink);letter-spacing:-.2px}
.header-phone{left:325px;top:42px;display:flex;align-items:center;gap:8px;font-size:7px;color:var(--ink);font-weight:600}
.header-divider{left:402px;top:36px;width:1px;height:30px;background:#ccc}
.header-address{left:415px;top:38px;display:flex;gap:9px;font-size:5px;line-height:10px;color:#555}
.header-address b{color:var(--ink)}
.btn-appointment{left:558px;top:40px;width:97px;height:24px;border-radius:3px;background:linear-gradient(#c9ac71,#8f7236);box-shadow:0 1px 3px rgba(0,0,0,.3);color:#fff;font-size:5.5px;font-weight:700;display:flex;align-items:center;justify-content:center;letter-spacing:.2px}

/* nav */
.main-nav{left:0;top:75px;width:755px;height:39px;background:linear-gradient(#333,#121212);border-bottom:2px solid var(--gold)}
.main-nav ul{list-style:none;display:flex;height:37px;align-items:center}
.main-nav li{font-size:7px;font-weight:700;color:#fff;padding:0 9px;height:37px;line-height:37px;border-right:1px solid #3d3d3d;position:relative;letter-spacing:-.15px;white-space:nowrap}
.main-nav li.active::after{content:"";position:absolute;left:50%;bottom:0;margin-left:-5px;border:5px solid transparent;border-bottom-color:var(--gold)}
.social{display:flex;gap:7px}
.social span{width:18px;height:18px;border:1px solid #555;background:#222;display:block}
.nav-social{left:670px;top:85px}

/* hero */
.hero{left:0;top:114px;width:755px;height:289px;background:linear-gradient(100deg,#7d8c6a 0%,#c8a488 25%,#8d7a66 45%,#c7b29c 65%,#d9c9b4 85%,#a39078 100%);overflow:hidden}
.hero-band{position:absolute;left:0;top:0}
.hero-caption{position:absolute;left:100px;top:256px;font-size:7.5px;font-weight:700;color:#fff;letter-spacing:.1px}
.hero-contact{position:absolute;left:580px;top:253px;width:74px;height:23px;border:1px solid #ddd;color:#fff;font-size:5.5px;font-weight:600;display:flex;align-items:center;justify-content:center}
.hero-panel{position:absolute;left:479px;top:38px;width:175px;height:150px;background:rgba(20,20,20,.78);color:#fff;padding:14px 11px}
.hero-panel h2{font-size:9.5px;font-weight:400;padding-bottom:8px;border-bottom:1px solid #888}
.hero-panel p{font-size:7px;line-height:13px;margin-top:9px;color:#eee}
.hero-panel .learn{position:absolute;left:0;right:0;top:106px;border-top:1px solid #666;text-align:center;padding-top:14px;font-size:7px;color:#bbb}

/* sections */
.section-title{position:absolute;left:99px;width:364px;border-bottom:2px solid var(--rule);height:34px}
.section-title h3{font-size:8.5px;font-weight:800;color:var(--ink);margin-top:-2px}
.section-title small{display:block;font-size:4.5px;color:var(--muted)}
.video{left:101px;top:479px;width:362px;height:188px;background:linear-gradient(110deg,#7f8f6b,#c9a78a 35%,#8f7b66 55%,#cdb9a2 80%,#9a8a72)}
.video-bar{position:absolute;left:0;bottom:0;width:100%;height:17px;background:linear-gradient(#2a2a2a,#050505);color:#ddd;font-size:6px}
.video-track{position:absolute;left:24px;top:7px;width:192px;height:3px;background:#555;border-radius:2px}
.video-track i{position:absolute;left:0;top:0;width:44px;height:3px;background:#aaa}
.rate-btn{width:158px;height:62px;border-radius:4px;background:linear-gradient(#c3a56a,#8e7036);box-shadow:0 1px 3px rgba(0,0,0,.3);color:#fff;text-align:center;padding-top:11px}
.rate-btn small{display:block;font-size:9px;font-weight:700;color:#f3e6c8}
.rate-btn strong{display:block;font-size:22px;font-weight:700;line-height:26px}
.copy{left:99px;width:364px;font-size:4.6px;line-height:9.8px;color:#666}
.read-more{font-size:5px;color:var(--muted);text-decoration:underline}
.card{width:175px;height:127px;border:1px solid #ddd;border-radius:3px;box-shadow:0 1px 2px rgba(0,0,0,.1);overflow:hidden}
.card-img{height:61px}
.card h4{font-size:7.5px;font-weight:700;color:var(--ink);margin:6px 0 0 4px}
.card p{font-size:5.5px;line-height:10px;color:#666;margin:3px 4px 0 4px}
.card .read-more{position:absolute;right:22px;bottom:8px}

/* sidebar */
.side-box{left:479px;width:175px;border:1px solid #ccc}
.side-head{background:var(--ink);color:#fff;font-size:7.5px;font-weight:700;text-align:center}
.hours{list-style:none;padding:6px 9px}
.hours li{display:flex;justify-content:space-between;font-size:6px;height:13.8px;color:#333}
.hours li.closed{color:var(--gold)}
.consult-head{position:relative;height:52px;padding-top:9px;text-align:center;font-size:7.5px;line-height:14px}
.consult-head .g{color:var(--gold)}
.consult-head .w{color:#fff;font-weight:700}
.form{padding:8px 9px}
.form h5{font-size:7px;font-weight:800;color:var(--ink);margin-bottom:11px}
.form label{display:block;font-size:6px;color:#333;margin-bottom:2px}
.form .field{height:13px;border:1px solid #bbb;margin-bottom:13px}
.form .field.tall{height:47px}
.submit{width:60px;height:20px;background:linear-gradient(#c3a56a,#8e7036);border-radius:2px;color:#f3e6c8;font-size:6.5px;font-weight:700;display:flex;align-items:center;justify-content:center;letter-spacing:.6px}
.testimonial{text-align:center}
.testimonial p{font-size:4.6px;line-height:10px;color:#555;padding:24px 10px 0}
.testimonial cite{display:block;font-size:8px;color:var(--ink);margin-top:10px}
.arrow-btn{position:absolute;width:19px;height:17px;background:linear-gradient(#c3a56a,#8e7036);color:#fff;font-size:9px;line-height:17px;text-align:center}

/* footer */
.footer-top{left:0;top:1124px;width:755px;height:36px;background:var(--footer-grey)}
.footer-bottom{left:0;top:1160px;width:755px;height:40px;background:var(--footer-gold)}
.footer-legal{left:100px;top:1171px;font-size:4.8px;line-height:10px;color:#fff}
.footer-nav{left:252px;top:1182px;display:flex;list-style:none;font-size:5px;color:#fff;font-weight:600;white-space:nowrap}
.footer-nav li{padding:0 4px;border-left:1px solid rgba(255,255,255,.4)}
.footer-nav li:first-child{border:0}
.to-top{left:637px;top:1173px;width:18px;height:19px;border:1px solid #ddd;color:#fff;font-size:8px;text-align:center;line-height:17px}
</style>
</head>
<body>

<!-- header -->
<header>
  <div class="brand" style="left:99px;top:32px"><span class="brand-square"></span><span class="brand-name">BRIGHTMOOR</span></div>
  <div class="abs header-phone">
    <svg width="11" height="11" viewBox="0 0 24 24"><path fill="#111" d="M6.6 10.8a15 15 0 0 0 6.6 6.6l2.2-2.2c.3-.3.7-.4 1-.2 1.1.4 2.3.6 3.6.6.6 0 1 .4 1 1V20c0 .6-.4 1-1 1A17 17 0 0 1 3 4c0-.6.4-1 1-1h3.5c.6 0 1 .4 1 1 0 1.3.2 2.5.6 3.6.1.3 0 .7-.2 1z"/></svg>
    <span>555-014-2739</span>
  </div>
  <div class="abs header-divider"></div>
  <div class="abs header-address">
    <svg width="16" height="14" viewBox="0 0 24 22"><path fill="#111" d="M12 1 1 11h3v10h6v-6h4v6h6V11h3z"/></svg>
    <div>4128 North Tamsin Blvd, Suite #7<br><b>HARROWFIELD, GA 30917</b></div>
  </div>
  <a class="abs btn-appointment">MAKE AN APPOINTMENT</a>
</header>

<nav class="abs main-nav">
  <ul>
    <li>HOME</li>
    <li class="active">WHY BRIGHTMOOR?</li>
    <li>HOW CHIROPRACTIC HELPS</li>
    <li>ASK THE DOCTOR</li>
    <li>WORK PLACE WELLNESS</li>
    <li>REQUEST AN APPOINTMENT</li>
    <li>BLOG</li>
    <li>CONTACT US</li>
  </ul>
</nav>
<div class="abs social nav-social">
  <span aria-label="Chatterly"></span><span aria-label="Vexora+"></span><span aria-label="Streamlo"></span>
</div>

<!-- hero -->
<section class="abs hero" role="img" aria-label="Photo of friends laughing together over an outdoor dinner">
  <svg class="hero-band" width="755" height="289" viewBox="0 0 755 289">
    <path d="M0 226 Q 380 196 755 232 L755 289 L0 289 Z" fill="rgba(28,28,28,.78)"/>
  </svg>
  <div class="hero-panel">
    <h2>Quam eleifend metus commodo</h2>
    <p>luctus at sit amet urna. Quisque non augue as massa non, elementum sem. Suspendiss eu lorem ultricies dapibus.</p>
    <div class="learn">Learn more &rsaquo;</div>
  </div>
  <div class="hero-caption">QUAM ELEIFEND METUS COMMODO &nbsp;UCTUS AT SIT AMET URNA &nbsp;QUISQUE NON AUGUE TINCIDUNT EG</div>
  <div class="hero-contact">Contact Us &nbsp;&#9993;</div>
</section>

<!-- left column -->
<div class="section-title" style="top:440px"><h3>OUR VIDEOS</h3><small>Lorem ipsum dolor sit amet, consed</small></div>
<div class="abs video" role="img" aria-label="Video still of friends sharing a meal outdoors">
  <div class="video-bar">
    <svg class="abs" style="left:8px;top:4px" width="8" height="9" viewBox="0 0 8 9"><path d="M0 0 8 4.5 0 9z" fill="#ddd"/></svg>
    <div class="video-track"><i></i></div>
    <span class="abs" style="left:229px;top:3px">1:30 - 4:23</span>
    <span class="abs" style="left:265px;top:7px;width:44px;height:3px;background:#777;border-radius:2px"></span>
  </div>
</div>
<div class="abs rate-btn" style="left:99px;top:690px"><small>RATE US ON:</small><strong>Vexora</strong></div>
<div class="abs rate-btn" style="left:304px;top:690px"><small>FIND US ON:</small><strong>Chatterly</strong></div>

<div class="section-title" style="top:776px;height:26px"><h3>WELCOME LETTER</h3><small>Lorem ipsum dolor sit amet, consed</small></div>
<p class="abs copy" style="top:804px">Sed ut perspiciatis unde omnis iste natus error sit voluptatem accusantium doloremque laudantium, totam rem aperiam, eaque ipsa quae ab illo inventore veritatis et quasi architecto beatae vitae dicta sunt.</p>
<p class="abs copy" style="top:832px">Neque porro quisquam est, qui dolorem ipsum quia dolor sit amet, consectetur, adipisci velit, sed quia non numquam eius modi tempora incidunt ut labore et dolore magnam aliquam quaerat voluptatem. Ut enim ad minima veniam, quis nostrum exercitationem ullam corporis suscipit laboriosam, nisi ut aliquid ex ea commodi consequatur. Quis autem vel eum iure reprehenderit qui in ea voluptate velit esse quam nihil molestiae consequatur, vel illum qui dolorem eum fugiat quo voluptas nulla pariatur at vero eos et accusamus.</p>
<span class="abs read-more" style="left:421px;top:877px">Read More &rsaquo;</span>

<div class="section-title" style="top:899px;height:27px"><h3>WELCOME LETTER</h3><small>Lorem ipsum dolor sit amet, consed</small></div>
<article class="abs card" style="left:99px;top:939px">
  <div class="card-img" role="img" aria-label="Photo of fresh oranges, apples and carrots" style="background:linear-gradient(100deg,#e9d9a8,#f1b84a 45%,#e7d27a 75%,#9cbd5a)"></div>
  <h4>LOREM IPSUM DOLOR</h4>
  <p>Neque porro quisquam est, qui dolorem ipsum quia dolor sit ametNeque porro quisquam est, qui dolorem ipsum qu ia dolor sit amet</p>
  <span class="read-more">Read More &rsaquo;</span>
</article>
<article class="abs card" style="left:288px;top:939px">
  <div class="card-img" role="img" aria-label="Photo of a smiling family" style="background:linear-gradient(100deg,#a88f72,#d8b59a 40%,#c59c80 70%,#8e7763)"></div>
  <h4>LOREM IPSUM DOLOR</h4>
  <p>Neque porro quisquam est, qui dolorem ipsum quia dolor sit ametNeque porro quisquam est, qui dolorem ipsum qu ia dolor sit amet</p>
  <span class="read-more">Read More &rsaquo;</span>
</article>

<!-- right column -->
<aside class="abs side-box" style="top:440px;height:140px">
  <div class="side-head" style="height:28px;line-height:28px">OFFICE HOURS</div>
  <ul class="hours">
    <li><span>Monday:</span><span>8:00-11:00, 2:00-5:00</span></li>
    <li><span>Tuesday:</span><span>8:30-11:00, 2:00-5:30</span></li>
    <li><span>Wednesday</span><span>8:00-11:00, 2:00-5:00</span></li>
    <li><span>Thursday:</span><span>10:00-12:00, 2:30-5:00</span></li>
    <li><span>Friday:</span><span>8:00-10:00, 1:00-5:00</span></li>
    <li class="closed"><span>Saturday:</span><span>Closed</span></li>
    <li class="closed"><span>Sunday:</span><span>Closed</span></li>
  </ul>
</aside>

<aside class="abs side-box" style="top:594px;height:291px">
  <div class="side-head consult-head">
    <div class="g">CONTACT US NOW &amp; GET YOUR</div>
    <div class="w">FREE CONSULTATION</div>
    <div class="g">TODAY !</div>
    <svg class="abs" style="left:0;top:0" width="173" height="66" viewBox="0 0 173 66">
      <path d="M38 43H68M105 43H135" stroke="#777" stroke-width=".6"/>
      <path d="M0 52 86.5 66 173 52" fill="var(--ink)"/>
    </svg>
  </div>
  <div class="form" style="padding-top:18px">
    <h5>WELLNESS BEGINS HERE</h5>
    <label>First Name</label><div class="field"></div>
    <label>Last Name</label><div class="field"></div>
    <label>Phone Number</label><div class="field"></div>
    <label>Comments</label><div class="field tall"></div>
    <div class="submit">SUBMIT &rsaquo;</div>
  </div>
</aside>

<aside class="abs side-box" style="top:900px;height:165px;border-color:#ddd">
  <div class="side-head" style="height:28px;line-height:28px">PATIENT TESTEMONIALS</div>
  <div class="testimonial">
    <p>&ldquo; veniam, quis nostrum exercitationem ullam Ut enim adveniam,<br>veniam, quis nostrum exercitationem ullam Ut enim adveniam &rdquo;</p>
    <cite>-Marla Venn -</cite>
  </div>
  <div class="arrow-btn" style="left:19px;top:97px">&lsaquo;</div>
  <div class="arrow-btn" style="left:134px;top:97px">&rsaquo;</div>
  <svg class="abs" style="left:0;top:106px" width="173" height="17" viewBox="0 0 173 17">
    <path d="M0 15H78L86.5 3 95 15H173V17H0Z" fill="var(--gold)"/>
  </svg>
  <div class="abs side-head" style="left:0;top:122px;width:173px;height:42px;line-height:42px;font-weight:600;color:#ccc">Read more &rsaquo;</div>
</aside>

<!-- footer -->
<footer>
  <div class="abs footer-top"></div>
  <div class="brand" style="left:99px;top:1131px"><span class="brand-square"></span><span class="brand-name">BRIGHTMOOR</span></div>
  <div class="abs social" style="left:585px;top:1134px">
    <span aria-label="Chatterly" style="background:#444;border-color:#444"></span><span aria-label="Vexora+" style="background:#444;border-color:#444"></span><span aria-label="Streamlo" style="background:#444;border-color:#444"></span>
  </div>
  <div class="abs footer-bottom"></div>
  <div class="abs footer-legal">4128 North Tamsin Blvd, Suite #7, HARROWFIELD, GA 30917<br>Powered by Pixelmere Web Group &copy; Copyright 2015</div>
  <ul class="abs footer-nav">
    <li>Home</li><li>Why Brightmoor?</li><li>How Chiropractic Helps</li><li>Ask the Doctor</li><li>Work Place Wellness</li><li>Request an Appointment</li><li>Blog</li><li>Contact Us</li>
  </ul>
  <div class="abs to-top">&#8963;</div>
</footer>

</body>
</html>
```